Need innovative card design for tech start up

We are a Santa Monica based marketing analytics software start up called Meridel Pulse. We're launching a platform that will help advertisers better measure and optimize their marketing spend by using advanced algorithmic analytic. While our subject matter is complicated, we want to convey simple, clean, curated. We also want to stand out - ad tech is a sea of sameness and we need to have some individuality. We have an established color palette and would like to see a design we could print in each tone (teal, tangerine, grey), but it doesn't require the card to be monochromatic. The font used is DENSE.

Marketing

```html
<!DOCTYPE html>
<html lang="en">
<head>
<meta charset="utf-8">
<title>Meridel Pulse — Business Card</title>
<link rel="stylesheet" href="https://fonts.googleapis.com/css2?family=Oswald:wght@300;400&display=swap">
<style>
  :root {
    --backdrop: #e9e7e4;
    --card-dark: #59595b;
    --card-white: #fbfbfb;
    --ink-grey: #8a8a8c;
    --tangerine: #e8901a;
    --gold: #d9a10f;
    --slate: #5f5f61;
    --name-white: #f2f2f2;
  }
  html, body {
    margin: 0;
    width: 1200px;
    height: 900px;
    overflow: hidden;
    background: var(--backdrop);
    font-family: "Oswald", "Arial Narrow", sans-serif;
  }
  .stage {
    position: relative;
    width: 1200px;
    height: 900px;
  }
  .card {
    position: absolute;
    left: 300px;
    width: 600px;
    height: 340px;
    box-shadow: 0 6px 18px rgba(0,0,0,0.18);
  }
  .card-back {
    top: 70px;
    background: var(--card-dark);
    border-radius: 4px 120px 4px 4px;
  }
  .card-front {
    top: 480px;
    border-radius: 120px 4px 4px 4px;
    overflow: hidden;
    background: var(--card-white);
  }
  .back-plate {
    position: absolute;
    left: 70px;
    top: 115px;
    width: 150px;
    height: 110px;
    background: #ffffff;
    display: flex;
    align-items: center;
    justify-content: center;
  }
  .wordmark {
    font-weight: 400;
    color: var(--ink-grey);
    letter-spacing: 1px;
    text-transform: uppercase;
    white-space: nowrap;
  }
  .back-plate .wordmark { font-size: 15px; }
  .front-art {
    position: absolute;
    inset: 0;
  }
  .front-brand {
    position: absolute;
    top: 62px;
    left: 0;
    width: 600px;
    display: flex;
    align-items: center;
    justify-content: center;
    gap: 10px;
  }
  .brand-square {
    width: 22px;
    height: 22px;
    background: var(--tangerine);
  }
  .front-brand .wordmark { font-size: 20px; }
  .holder-name {
    position: absolute;
    left: 52px;
    top: 240px;
    margin: 0;
    font-weight: 300;
    font-size: 44px;
    line-height: 1;
    color: var(--name-white);
  }
  .holder-title {
    position: absolute;
    left: 185px;
    top: 292px;
    margin: 0;
    font-weight: 300;
    font-size: 14px;
    color: #d8d8d8;
  }
  .contact {
    position: absolute;
    left: 420px;
    top: 206px;
    margin: 0;
    padding: 0;
    list-style: none;
    font-weight: 300;
    font-size: 12px;
    color: var(--slate);
    line-height: 20px;
  }
  .contact li { display: flex; align-items: center; gap: 7px; }
  .contact svg { width: 10px; height: 10px; }
</style>
</head>
<body>
<main class="stage">

  <section class="card card-back" aria-label="Card back">
    <div class="back-plate">
      <span class="wordmark">Meridel Pulse</span>
    </div>
  </section>

  <section class="card card-front" aria-label="Card front">
    <svg class="front-art" viewBox="0 0 600 340" width="600" height="340" aria-hidden="true">
      <polygon points="0,222 290,222 410,268 410,340 0,340" fill="var(--card-dark)"/>
      <rect x="410" y="268" width="80" height="24" fill="var(--gold)"/>
      <rect x="490" y="268" width="70" height="24" fill="var(--slate)"/>
      <rect x="560" y="268" width="40" height="24" fill="var(--tangerine)"/>
    </svg>

    <div class="front-brand">
      <span class="brand-square"></span>
      <span class="wordmark">Meridel Pulse</span>
    </div>

    <ul class="contact">
      <li>
        <svg viewBox="0 0 10 10" aria-hidden="true"><rect x="2" y="0.5" width="6" height="9" rx="1" fill="none" stroke="var(--tangerine)" stroke-width="1.3"/></svg>
        0455 210 684
      </li>
      <li>
        <svg viewBox="0 0 10 10" aria-hidden="true"><circle cx="5" cy="5" r="4" fill="none" stroke="var(--tangerine)" stroke-width="1.3"/><circle cx="5" cy="5" r="1.6" fill="var(--tangerine)"/></svg>
        darakellen@meridelpulse.com
      </li>
    </ul>

    <h1 class="holder-name">Dara Kellen</h1>
    <p class="holder-title">general manager</p>
  </section>

</main>
</body>
</html>
```